Diverse business needs a corporate identity system

Brantow Fielding Holdings Limited is a well established family owned and run business operating in Port Moresby, Papua New Guinea since 1989. As part of taking the business to the next level, we are redoing our branding/corporate identity.

We currently carry out two core business activities servicing corporate clients in the commercial and industrial sectors:
1. Electrical - new installations and maintenance work
2. Construction - mostly commercial & industrial, some residential

We are looking to add the following business activities in near future:
1. IT consulting
2. Property development - business/industrial park, residential complexes, low cost housing
3. Retail of hardware, construction supplies and flat pack furniture & kitchens

We have just completed our logo design here on SketchHarbor and now wanting to design business card and stationery based on our new logo (attached).

Deliverables are:
1. Business card - double sided
2. Letterhead A4

Details to go on the card:
Name: Marcus Trevane
Title: Director
Email: marcus.trevane@brantowfield.com
Tel: +675 3147720, +675 3148815
Office: Section 17 Lot 48, Waravu Light Industrial Area, Port Moresby, Papua New Guinea
Postal: PO Box 419, Waravu, NCD, Papua New Guinea
Website: brantowfield.com

Our services can be listed somewhere on the card:
Electrical, Construction, Property Development, IT Consulting

Details to go on the letterhead:
Brantow Fielding Holdings Ltd.
PO Box 419, Waravu, NCD, Papua New Guinea
Fax: +675 3146603
Email: info@brantowfield.com

For inspiration, I have uploaded some images of business cards we like.

Would be good if the same/similar business card design could be printed both economically (e.g. full coloured both sides, matte card stock) for majority of staff and upscaled to use premium features such as letter pressed, foil etc for use by executives. Otherwise, please provide two separate designs.

Logo text font is nexa bold freefont - please use something from nexa family or another font type that complements it.

Reason: Few designs were submitted. Most were clearly from ready to use templates. No designs really stand out for us at the moment. So we have decided to narrow the focus to just business card and A4 letterhead. And also revised the brief to be completely open to hopefully invite more creative designs.

I have updated the brief to be a lot less restrictive to try and get more creative designs. Also uploaded more images of premium business cards for inspiration.

Industry/Entity Type

Construction

Requirements
Must have
• All designs must conform to printolane specifications. Refer to and download appropriate work file templates from http://www.printolane.com.au/pl/ns/files/UploadResources.aspx?GP=1%2F9%2F2014+12%3A53%3A21+AM&GPS=5829104463&GNF=1&selectedTab=0.
Should not have
• No QR codes and social media links.

```html
<!DOCTYPE html>
<html lang="en">
<head>
<meta charset="utf-8">
<title>Brantow Fielding – Business Card</title>
<link href="https://fonts.googleapis.com/css2?family=Exo+2:wght@400;500;700&display=swap" rel="stylesheet">
<style>
  :root {
    --page-bg: #e9e7e3;
    --card-white: #f7f7f7;
    --card-dark: #1c1c1c;
    --card-dark-light: #3b3b3b;
    --accent-red: #e2412e;
    --ink: #1f1f1f;
    --name-white: #ffffff;
    --title-grey: #e4e4e4;
  }
  * { margin: 0; padding: 0; box-sizing: border-box; }
  html, body {
    width: 1200px;
    height: 1085px;
    overflow: hidden;
    background: var(--page-bg);
    font-family: "Exo 2", sans-serif;
  }
  .business-card {
    position: absolute;
    left: 75px;
    top: 242px;
    width: 1050px;
    height: 600px;
    background: var(--card-white);
    box-shadow: 0 10px 30px rgba(0,0,0,0.18);
    overflow: hidden;
  }
  .card-shapes {
    position: absolute;
    inset: 0;
    width: 100%;
    height: 100%;
  }
  .contact-block {
    position: absolute;
    right: 545px;
    text-align: right;
    color: var(--ink);
    font-size: 24px;
    font-weight: 500;
    line-height: 30px;
    letter-spacing: 0.5px;
  }
  .contact-phone { top: 118px; }
  .contact-address { top: 255px; }
  .contact-web { top: 420px; }
  .brand {
    position: absolute;
    left: 668px;
    top: 200px;
    display: flex;
    align-items: center;
    gap: 14px;
  }
  .brand-dot {
    width: 40px;
    height: 40px;
    border-radius: 50%;
    background: var(--accent-red);
    flex: none;
  }
  .brand-name {
    font-size: 36px;
    font-weight: 700;
    color: var(--accent-red);
    white-space: nowrap;
  }
  .person {
    position: absolute;
    left: 722px;
    top: 300px;
  }
  .person-name {
    font-size: 27px;
    font-weight: 500;
    letter-spacing: 1.5px;
    color: var(--name-white);
  }
  .person-title {
    margin-top: 4px;
    font-size: 21px;
    font-weight: 400;
    color: var(--title-grey);
    padding-left: 30px;
  }
</style>
</head>
<body>
  <div class="business-card">
    <svg class="card-shapes" viewBox="0 0 1050 600" aria-hidden="true">
      <defs>
        <linearGradient id="darkPanel" x1="0" y1="0" x2="1" y2="1">
          <stop offset="0" stop-color="var(--card-dark)"/>
          <stop offset="0.55" stop-color="var(--card-dark-light)"/>
          <stop offset="1" stop-color="var(--card-dark)"/>
        </linearGradient>
      </defs>
      <rect class="dark-panel" x="0" y="0" width="1050" height="600" fill="url(#darkPanel)"/>
      <path class="light-panel" fill="var(--card-white)"
        d="M0 0 H515 C515 70 622 80 622 150 C622 205 575 210 575 225 C575 240 622 245 622 300 C622 355 575 360 575 375 C575 390 622 395 622 450 C622 520 515 530 515 600 H0 Z"/>
      <g class="contact-icons" fill="none" stroke="var(--accent-red)" stroke-width="3">
        <circle cx="560" cy="150" r="26"/>
        <circle cx="560" cy="300" r="26"/>
        <circle cx="560" cy="450" r="26"/>
        <!-- phone -->
        <path d="M551 139 c-4 3 -3 10 3 17 s12 9 15 5 l2 -3 -6 -5 -3 3 c-3 -1 -7 -5 -8 -8 l3 -3 -5 -6 z" stroke-width="2.5" stroke-linejoin="round"/>
        <!-- pin -->
        <path d="M560 314 c-7 -9 -11 -14 -11 -20 a11 11 0 0 1 22 0 c0 6 -4 11 -11 20 z" fill="var(--accent-red)" stroke="none"/>
        <circle cx="560" cy="294" r="4" fill="var(--card-white)" stroke="none"/>
        <!-- globe -->
        <circle cx="560" cy="450" r="14" stroke-width="2.5"/>
        <ellipse cx="560" cy="450" rx="6" ry="14" stroke-width="2"/>
        <line x1="546" y1="450" x2="574" y2="450" stroke-width="2"/>
        <line x1="548" y1="443" x2="572" y2="443" stroke-width="2"/>
        <line x1="548" y1="457" x2="572" y2="457" stroke-width="2"/>
      </g>
    </svg>

    <div class="contact-block contact-phone">
      <p>014 527 3390</p>
      <p>014 527 3390</p>
    </div>
    <div class="contact-block contact-address">
      <p>047.12th floor,</p>
      <p>Harbor Crest Road</p>
      <p>KTV</p>
    </div>
    <div class="contact-block contact-web">
      <p>yourname@mailhost.com</p>
      <p>yourdomainhere.com</p>
    </div>

    <div class="brand">
      <span class="brand-dot"></span>
      <span class="brand-name">Brantow Fielding</span>
    </div>

    <div class="person">
      <p class="person-name">DORIAN WELLES</p>
      <p class="person-title">Managing Director</p>
    </div>
  </div>
</body>
</html>
```